Zielgruppe
Wir sind ein Vertriebsunternehmen, mit dem Ziel die klassische Finanz und den Kryptosektor zu verbinden. Unsere Zielgruppe sind Menschen zwischn 25 - 45 Jahre. Wir sind die Communty und Vertrieb der ersten rechtkonformen STO - Plattform ( Plattform für Wertpapiere im Kryptosektor)
Diese Projekt ist Teil eines Paketes, wir bitten nur Designer mit zu machen die alle benötigten Unterlagen designen können. (siehe restliche Projekte) - Gesamtvolumen: 2300€ Preisgeld
Online-Marketing Material
2 Vorlagen Social Media - (Einladung/Event, Sprüche/Information)
Banner
Präsentationsvorlagen - min unterschiedliche 8 Vorlagenseiten /Layouts.
Landingpage Layout f. Funnelsite für Webinaranmeldung mit Platz für Formular
Newsletter Layoutvorlage
Vorlage Infografik
Broschüre / E - Book Designe
Es werden nur Vorlagen benötigt mit 'LoremSum Texten' und Musterbildern. Wir möchten von allen Vorlagen die Originaldatei, uns stehen folgende Grafikprogramme zur Verfügung:
Adobe Photoshop
Adobe Illustrator
Canva
Newsletter und Landingpage Software: postwelle.com
Unsere Akt. Designe (Designe Alt) gefällt uns von der Idee, dennoch wünschen wir es uns moderner und edler mit ein wenig 'spaceig'. - Eben die Vereinigung von Kryptowelt und klassischer Finanz.
Schriftart: Poppins
Farben lt. Logo
Aufgabenstellung
Die Landingpage Layout f. Funnelsite für Webinaranmeldung mit Platz für Formular - Die Landingpage ersetzt nicht unsere aktuelle Website - sondern dient zur Leadgenerierung im Socialmedia Bereich.

```html
<!DOCTYPE html>
<html lang="en">
<head>
<meta charset="utf-8">
<title>GreenMarten Investments – Webinar Landing Page</title>
<link rel="stylesheet" href="https://fonts.googleapis.com/css2?family=Poppins:wght@400;500;600;700&display=swap">
<style>
  :root {
    --navy: #213f8f;
    --blue: #1f6fb2;
    --sky: #45b3e0;
    --green: #2bb673;
    --grey: #dedede;
    --ink: #111111;
    --white: #ffffff;
    --font: "Poppins", sans-serif;
  }
  * { margin: 0; padding: 0; box-sizing: border-box; }
  html, body { width: 1200px; height: 2399px; overflow: hidden; background: var(--white); font-family: var(--font); color: var(--ink); }
  .page { position: relative; width: 1200px; height: 2399px; overflow: hidden; }
  .abs { position: absolute; }

  .top-band { left: 0; top: 0; width: 1200px; height: 47px; background: var(--navy); }
  .hero-photo { left: 0; top: 47px; width: 1200px; height: 337px; background: linear-gradient(100deg, #b9c3d3 0%, #d8dde5 45%, #c9d3e2 75%, #9fb2d0 100%); }
  .hero-squares { left: 942px; top: 161px; display: flex; gap: 12px; }
  .hero-squares span { width: 31px; height: 31px; background: var(--blue); display: block; }
  .hero-bar { left: 0; top: 209px; width: 1200px; height: 148px; background: var(--white); }
  .brand-mark { left: 110px; top: 232px; width: 110px; height: 110px; background: var(--navy); }
  .hero-title { left: 289px; top: 272px; font-size: 22px; font-weight: 700; color: var(--navy); letter-spacing: -0.2px; white-space: nowrap; }

  .column { left: 178px; width: 881px; }
  .grey { background: var(--grey); }

  .tokens { top: 417px; height: 414px; background: var(--white); border-top: 2px solid var(--blue); }
  .tokens-pattern { left: 700px; top: 0; width: 181px; height: 412px; background: linear-gradient(90deg, rgba(255,255,255,0) 0%, #e6f1fa 100%); }
  .token { position: absolute; top: 46px; width: 190px; }
  .token svg.frame { position: absolute; left: 0; top: 26px; }
  .token .hanger { position: absolute; top: -46px; width: 2px; height: 38px; background: #444; }
  .token .clip { position: absolute; top: -10px; width: 16px; height: 12px; background: #222; border-radius: 2px; }
  .token .tab { position: absolute; left: 36px; top: 0; width: 118px; height: 58px; color: var(--white); font-size: 13px; font-weight: 600; line-height: 14px; text-align: center; padding-top: 16px; }
  .token .copy { position: absolute; left: 26px; top: 78px; width: 138px; font-size: 10px; line-height: 11.4px; text-align: center; }
  .token .copy p + p { margin-top: 11px; }

  .feature { top: 872px; height: 452px; background: var(--white); }
  .feature-photo { left: 0; top: 0; width: 454px; height: 452px; background: linear-gradient(135deg, #9aa7b3 0%, #c6ced6 45%, #a69080 100%); }
  .feature h2 { left: 488px; top: 26px; font-size: 30px; font-weight: 600; }
  .feature p { left: 491px; top: 96px; width: 370px; font-size: 16.4px; line-height: 20.2px; letter-spacing: -0.15px; }
  .btn { left: 652px; top: 382px; width: 198px; height: 48px; background: var(--blue); color: var(--white); border-radius: 5px; font-size: 16px; font-weight: 600; display: flex; align-items: center; justify-content: center; }

  .signup { top: 1343px; height: 184px; background: var(--blue); }
  .signup h2 { left: 59px; top: 36px; font-size: 51px; line-height: 56px; font-weight: 600; color: var(--white); }
  .signup .field { left: 428px; top: 93px; width: 422px; height: 65px; background: var(--white); border-radius: 10px; }

  .brand-block { top: 1546px; height: 158px; }
  .brand-dot { left: 115px; top: 50px; width: 62px; height: 62px; background: var(--navy); border-radius: 50%; }
  .brand-name { left: 190px; top: 56px; font-size: 36px; font-weight: 600; color: var(--navy); white-space: nowrap; line-height: 50px; }

  .team { top: 1722px; height: 401px; background: var(--white); border-right: 1px solid var(--grey); }
  .portrait { position: absolute; top: 71px; width: 149px; height: 149px; border-radius: 50%; background: radial-gradient(circle at 50% 40%, #d9d9d9 0%, #8a8a8a 70%, #3a3a3a 100%); }
  .caption { position: absolute; top: 262px; width: 340px; text-align: center; font-size: 17px; line-height: 20px; }
  .caption strong { font-weight: 600; display: block; }

  .footer { left: 0; top: 2152px; width: 1200px; height: 218px; background: var(--navy); }
</style>
</head>
<body>
<div class="page">
  <div class="abs top-band"></div>
  <div class="abs hero-photo" role="img" aria-label="Photo of a hand with a pen over financial charts"></div>
  <div class="abs hero-squares"><span></span><span></span><span></span></div>
  <div class="abs hero-bar"></div>
  <div class="abs brand-mark" role="img" aria-label="GreenMarten logo placeholder"></div>
  <h1 class="abs hero-title">LOREM IPSUM DOLOR SIT AMET, CONSECTETUER ADIPISCING ELIT, SED</h1>

  <div class="abs column grey" style="top:384px;height:33px;"></div>

  <section class="abs column tokens">
    <div class="abs tokens-pattern" role="img" aria-label="Soft hexagon pattern background"></div>

    <div class="token" style="left:109px;">
      <span class="hanger" style="left:55px"></span><span class="hanger" style="left:135px"></span>
      <span class="clip" style="left:48px"></span><span class="clip" style="left:128px"></span>
      <svg class="frame" width="190" height="310" viewBox="0 0 190 310"><path d="M4 4 H186 V260 L95 306 L4 260 Z" fill="#fff" stroke="#45b3e0" stroke-width="6" stroke-linejoin="round"/></svg>
      <div class="tab" style="background:var(--sky)">VOLT<br>TOKEN</div>
      <div class="copy">
        <p>The VLT is connected to renewable electric energies and is driven by two businesses: Green Mining &amp; CO2 Neutral Energy Supplies.</p>
        <p>You are investing in modern ASIC mining machines as well as participating in a renewable highly efficient sector.</p>
        <p>With the VLT your annual profit is roughly 70% and payouts are done on a monthly basis direct to your BTC wallet.</p>
      </div>
    </div>

    <div class="token" style="left:346px;">
      <span class="hanger" style="left:55px"></span><span class="hanger" style="left:135px"></span>
      <span class="clip" style="left:48px"></span><span class="clip" style="left:128px"></span>
      <svg class="frame" width="190" height="310" viewBox="0 0 190 310"><path d="M4 4 H186 V260 L95 306 L4 260 Z" fill="#fff" stroke="#1f6fb2" stroke-width="6" stroke-linejoin="round"/></svg>
      <div class="tab" style="background:var(--blue)">ZEST<br>TOKEN</div>
      <div class="copy">
        <p>ZEST - The Vital is the world's first premium functional drink with an aphrodisiac and activating effect.</p>
        <p>The drink, which is unique on the market, was developed by a doctor from Salzburg/Austria.</p>
        <p>As an investor, you will receive a share of the sales of this beverage novelty, which will be launched on the market at the end of 2021</p>
      </div>
    </div>

    <div class="token" style="left:583px;">
      <span class="hanger" style="left:55px"></span><span class="hanger" style="left:135px"></span>
      <span class="clip" style="left:48px"></span><span class="clip" style="left:128px"></span>
      <svg class="frame" width="190" height="310" viewBox="0 0 190 310"><path d="M4 4 H186 V260 L95 306 L4 260 Z" fill="#fff" stroke="#2bb673" stroke-width="6" stroke-linejoin="round"/></svg>
      <div class="tab" style="background:var(--green)">REFORM<br>TOKEN</div>
      <div class="copy">
        <p>Plastic waste is a global environmental issue.</p>
        <p>The process of depolymerization breaks down plastic waste into valuable raw materials: crude oil, gas and activated carbon.</p>
        <p>In addition, CO2 certificates can be profitably marketed.</p>
        <p>With your reform token you benefit from freeing our world from plastic waste.</p>
      </div>
    </div>
  </section>

  <div class="abs column grey" style="top:831px;height:41px;"></div>

  <section class="abs column feature">
    <div class="abs feature-photo" role="img" aria-label="Photo of hands at a laptop with a digital checklist"></div>
    <h2 class="abs">Lorem ipsum</h2>
    <p class="abs">Lorem ipsum dolor sit amet, consectetuer adipiscing elit, sed diam nonummy nibh euismod tincidunt ut laoreet dolore magna aliquam erat volutpat. Ut wisi Lorem ipsum dolor sit amet, consectetuer adipiscing elit, sed diam nonummy nibh euismod tincidunt ut laoreet dolore magna aliquam erat volutpat. Ut wisi enim ad minim veniam, quis nostrud exerci tation ullamcorper suscipit lobortis nisl ut aliquip ex ea commodo consequat. Duis autem vel eum iriure dolor in hendrerit in vulputate velit esse molestie consequat,</p>
    <a class="abs btn">Lorem ipsum</a>
  </section>

  <div class="abs column grey" style="top:1324px;height:19px;"></div>

  <section class="abs column signup">
    <h2 class="abs">Lorem ipsum<br>dolor sit</h2>
    <div class="abs field"></div>
  </section>

  <div class="abs column grey" style="top:1527px;height:19px;"></div>

  <section class="abs column brand-block">
    <div class="abs brand-dot"></div>
    <div class="abs brand-name">GreenMarten Investments</div>
  </section>

  <div class="abs column grey" style="top:1704px;height:18px;"></div>

  <section class="abs column team">
    <div class="portrait" style="left:42px" role="img" aria-label="Black and white portrait of a team member"></div>
    <div class="portrait" style="left:225px" role="img" aria-label="Black and white portrait of a team member"></div>
    <div class="portrait" style="left:501px" role="img" aria-label="Black and white portrait of a team member"></div>
    <div class="portrait" style="left:685px" role="img" aria-label="Black and white portrait of a team member"></div>
    <div class="caption" style="left:37px"><strong>Lorem ipsum dolor</strong>sit amet, consectetuer adipiscing elit, sed diam nonummy nibh euismod</div>
    <div class="caption" style="left:494px"><strong>Lorem ipsum dolor</strong>sit amet, consectetuer adipiscing elit, sed diam nonummy nibh euismod</div>
  </section>

  <div class="abs column grey" style="top:2123px;height:29px;"></div>
  <div class="abs footer"></div>
  <div class="abs column grey" style="top:2370px;height:29px;"></div>
</div>
</body>
</html>
```